Our desktop web app builder needs a redesign

We want to redesign our low-code web app builder called Fernhold. Fernhold runs in desktop environments and is aimed at IT professionals and developers.

The UI consists of a button bar, multiple panels and a tabbed working area. We are looking to completely change the look and feel of the application interfaces, while keeping the layout and functionality the same.

We would like to see your ideas for fonts, sizing, colour, icons and any other visual UI element. Your work can be a rough mockup of your design ideas, and does not need to be pixel perfect. Legibility and optimised use of space are key.

More details about the app and how it works here: https://fernhold.software/

If we like your ideas, we will get in touch with you and work with you to develop the new design in greater detail.

```html
<!DOCTYPE html>
<html lang="en">
<head>
<meta charset="utf-8">
<title>Fernhold Designer – UI concept</title>
<link rel="stylesheet" href="https://fonts.googleapis.com/css2?family=Roboto:wght@400;500;700&family=Poppins:wght@600;700&display=swap">
<style>
:root{
  --cyan:#00b5d6;
  --cyan-soft:#8ed6e6;
  --page:#ebebeb;
  --panel:#f3f3f3;
  --white:#ffffff;
  --ink:#4a4a4a;
  --muted:#7b7b7b;
  --line:#e1e1e1;
  --bar:#8a8a8a;
  --error:#e0202a;
}
*{box-sizing:border-box;margin:0;padding:0}
html,body{width:1200px;height:3023px;overflow:hidden;background:var(--page);font-family:'Roboto',sans-serif;color:var(--ink)}
.abs{position:absolute}
.board{position:absolute;left:100px;width:1000px;background:var(--panel);overflow:hidden}

/* ---------- designer window ---------- */
.designer{top:88px;height:1047px}
.titlebar{left:11px;top:13px;width:978px;height:27px;background:var(--white);font-size:10px;display:flex;align-items:center}
.brand{display:flex;align-items:center;gap:5px;margin-left:9px;color:var(--cyan);font-size:13px;font-weight:400;letter-spacing:.3px;width:105px}
.brand i{width:9px;height:9px;border-radius:50%;background:var(--cyan);display:block}
.menus{display:flex;gap:10px;color:var(--ink)}
.doc-title{margin-left:48px;color:var(--ink)}
.win-ctrls{margin-left:auto;display:flex;height:100%}
.win-ctrls span{width:20px;border-left:1px solid var(--line);display:flex;align-items:center;justify-content:center;font-size:10px;color:var(--ink)}
.toolbar{left:11px;top:41px;width:978px;height:30px;background:var(--cyan);display:flex;align-items:center;padding-left:16px;gap:22px}
.toolbar svg{width:15px;height:15px;fill:none;stroke:var(--white);stroke-width:1.6}
.toolbar .right{margin-left:auto;display:flex;gap:16px;padding-right:14px}

.tab{height:29px;background:var(--cyan-soft);color:var(--white);font-size:10px;font-weight:500;display:flex;align-items:center;justify-content:center;letter-spacing:.2px}
.pane-ctrls{display:flex;gap:12px;font-size:10px;color:var(--ink)}

.explorer{left:11px;top:74px;width:220px;height:973px;background:var(--panel)}
.tree{font-size:11px;color:var(--ink)}
.tree div{position:absolute;display:flex;align-items:center;gap:8px;white-space:nowrap}
.tree b{font-weight:400;font-size:7px;color:var(--ink);width:8px}
.tree em{display:block;width:9px;height:10px;border:1.4px solid #777;border-radius:1px}

.canvas{left:232px;top:74px;width:507px;height:694px;background:var(--white)}
.canvas h2{position:absolute;top:10px;width:100%;text-align:center;font-size:11px;font-weight:500;color:var(--cyan)}
.sep{position:absolute;left:0;width:507px;height:1px;background:var(--line)}
.chip{position:absolute;height:35px;background:var(--cyan);color:var(--white);font-size:11px;font-weight:500;display:flex;align-items:center;gap:14px;padding-left:14px;border-radius:1px}
.chip.tail::after{content:"";position:absolute;right:-6px;top:13px;border:5px solid transparent;border-left:6px solid var(--cyan);border-right:0}
.chip.sel::before{content:"";position:absolute;left:50%;bottom:-6px;border:6px solid transparent;border-top:6px solid var(--cyan);border-bottom:0;margin-left:-6px}
.cell{position:absolute;width:129px;height:38px;border:1px solid var(--line);background:var(--white);font-size:11px;display:flex;align-items:center;padding-left:10px;gap:18px;color:var(--ink)}
.cell.strong{font-weight:500;letter-spacing:.2px}
.tglyph{width:13px;height:12px}

.validations{left:232px;top:768px;width:511px;height:279px;background:var(--panel)}
.val-head{position:absolute;left:0;top:0;width:511px;height:33px;background:#e2e2e2}
.val-head .tab{position:absolute;left:0;top:0;width:130px;height:33px;background:var(--cyan-soft);font-size:12px}
.val-col-line{position:absolute;left:267px;top:33px;width:1px;height:246px;background:var(--line)}
.val-label{position:absolute;font-size:10px;font-weight:500;color:var(--ink)}
.val-row{position:absolute;font-size:11px;color:var(--ink);line-height:16px}
.val-row .x{color:var(--error);font-weight:700;margin-right:14px}

.toolbox{left:744px;top:74px;width:245px;height:973px;background:var(--panel)}
.viewbar{position:absolute;left:0;width:245px;height:15px;background:var(--bar);color:var(--white);font-size:7px;font-weight:700;padding-left:10px;display:flex;align-items:center}
.tools{position:absolute;left:0;display:grid;grid-template-columns:repeat(4,60px);column-gap:1.6px;row-gap:3px}
.tool{height:40px;background:var(--white);display:flex;flex-direction:column;align-items:center;justify-content:center;gap:6px;font-size:6.5px;font-weight:500;color:#333}
.tool i{display:block;width:8px;height:8px;border:1.5px solid #333;border-radius:1px}
.props-label{position:absolute;font-size:10px;color:var(--ink)}
.props-section{position:absolute;font-size:10px;font-weight:700;color:var(--cyan);left:19px}
.prop-input{position:absolute;height:35px;background:var(--white);font-size:10px;display:flex;align-items:center;padding-left:16px;color:var(--ink)}
.prop-check{position:absolute;width:20px;height:20px;background:var(--white)}
.help-btn{position:absolute;left:0;top:580px;width:245px;height:42px;background:var(--cyan);color:var(--white);font-size:13px;font-weight:700;display:flex;align-items:center;justify-content:center;letter-spacing:.2px}

/* ---------- column editor ---------- */
.editor{height:791px}
.editor.first{top:1242px}
.editor.second{top:2142px}
.ed-bar{left:38px;top:28px;width:924px;height:28px;background:var(--white);font-size:10px;font-weight:700;display:flex;align-items:center;padding-left:20px;color:#333}
.ed-bar .ctrls{margin-left:auto;display:flex;gap:18px;padding-right:18px;font-size:10px}
.add-col{left:38px;top:73px;width:130px;height:40px;background:var(--cyan);color:var(--white);font-size:11px;font-weight:700;display:flex;align-items:center;padding-left:14px;gap:20px}
.trash{left:458px;top:84px;width:16px;height:18px}
.field{position:absolute;left:38px;width:436px;height:39px;background:var(--white);font-size:12px;display:flex;align-items:center;padding:0 18px 0 19px;color:var(--ink)}
.field svg{margin-left:auto;width:12px;height:12px;fill:#555}
.group{position:absolute;left:555px;font-size:13px;font-weight:700;color:var(--cyan)}
.lbl{position:absolute;left:555px;font-size:11px;font-weight:700;color:#444}
.input{position:absolute;left:679px;width:280px;height:36px;background:var(--white);font-size:12px;display:flex;align-items:center;padding:0 16px;color:var(--ink)}
.input .chev{margin-left:auto;width:8px;height:5px}
.action{position:absolute;left:679px;width:280px;height:36px;background:var(--cyan);color:var(--white);font-size:11px;font-weight:700;display:flex;align-items:center;justify-content:center}
.checkbox{position:absolute;left:679px;width:45px;height:36px;background:var(--white);display:flex;align-items:center;justify-content:center}
.footer{position:absolute;left:0;top:597px;width:1000px;height:194px;background:var(--cyan);color:var(--white);text-align:center}
.footer h3{position:absolute;top:35px;width:100%;font-family:'Poppins',sans-serif;font-size:27px;font-weight:700;letter-spacing:.3px}
.footer p{position:absolute;top:83px;width:100%;font-size:10.5px;font-weight:700;letter-spacing:.1px}
.btn{position:absolute;top:121px;height:30px;font-size:11px;font-weight:700;display:flex;align-items:center;justify-content:center}
.btn.save{left:421px;width:71px;border:1.5px solid var(--white);color:var(--white)}
.btn.cancel{left:507px;width:71px;background:var(--white);color:var(--cyan)}
.expr-toggle{position:absolute;left:924px;width:35px;height:36px;background:var(--cyan);display:flex;align-items:center;justify-content:center}
.expr{position:absolute;left:679px;top:394px;width:280px;height:195px;background:var(--white);border:1.5px solid var(--cyan)}
.expr h4{position:absolute;left:19px;top:18px;font-size:14px;font-weight:500;color:#333}
.expr h4 sup{font-size:7px}
.expr .node{position:absolute;font-size:11px;color:var(--ink);display:flex;align-items:center;gap:10px}
.expr .node.active{color:var(--cyan)}
.expr .dot{width:8px;height:8px;border-radius:50%;border:2px solid var(--cyan)}
.caret{width:0;height:0;border:4px solid transparent;border-top:5px solid #555;border-bottom:0}
.caret.blue{border-top-color:var(--cyan)}
</style>
</head>
<body>

<!-- ================= Designer workspace ================= -->
<section class="board designer">
  <div class="abs titlebar">
    <div class="brand"><i></i>FERNHOLD</div>
    <div class="menus"><span>File</span><span>Edit</span><span>Insert</span><span>Run</span><span>Window</span><span>Help</span></div>
    <div class="doc-title">Appwithtable_stable.sapz - Fernhold Designer</div>
    <div class="win-ctrls"><span>↗</span><span>⊥</span><span>✕</span></div>
  </div>

  <div class="abs toolbar">
    <svg viewBox="0 0 16 16"><path d="M1 4h5l1 2h8v8H1z"/></svg>
    <svg viewBox="0 0 16 16"><rect x="1" y="3" width="14" height="10"/><path d="M4 6h4M4 9h4M10 6h2M10 9h2"/></svg>
    <svg viewBox="0 0 16 16"><path d="M3 1h7l3 3v11H3z"/></svg>
    <svg viewBox="0 0 16 16"><path d="M3 1h7l3 3v11H3z M6 10l2-4 2 4"/></svg>
    <svg viewBox="0 0 16 16"><circle cx="8" cy="8" r="6"/><circle cx="8" cy="8" r="3"/></svg>
    <svg viewBox="0 0 16 16"><rect x="1" y="2" width="14" height="12"/><path d="M1 6h14M1 10h14M6 2v12M10 2v12"/></svg>
    <svg viewBox="0 0 16 16"><rect x="1" y="5" width="14" height="9"/><path d="M5 5V2h6v3"/></svg>
    <svg viewBox="0 0 16 16"><path d="M3 13l10-10M5 3h-3v3M11 13h3v-3"/></svg>
    <svg viewBox="0 0 16 16"><path d="M4 2l10 6-10 6z" fill="#fff"/></svg>
    <svg viewBox="0 0 16 16"><path d="M13 8a5 5 0 1 1-2-4M13 2v3h-3"/></svg>
    <svg viewBox="0 0 16 16"><rect x="3" y="1" width="10" height="4"/><rect x="1" y="5" width="14" height="6"/><rect x="4" y="10" width="8" height="5"/></svg>
    <div class="right">
      <svg viewBox="0 0 16 16"><path d="M2 6h3l4-3v10l-4-3H2z M11 5q2 3 0 6"/></svg>
      <svg viewBox="0 0 16 16"><path d="M1 6l7-3 7 3-7 3z M4 8v3q4 2 8 0V8"/></svg>
      <svg viewBox="0 0 16 16"><circle cx="8" cy="8" r="7" fill="#fff"/><path d="M6 6q0-2 2-2t2 2-2 2v1M8 11v1" stroke="#00b5d6"/></svg>
    </div>
  </div>

  <!-- application explorer -->
  <aside class="abs explorer">
    <div class="tab abs" style="left:0;top:0;width:132px">APPLICATION EXPLORER</div>
    <div class="pane-ctrls abs" style="left:161px;top:9px"><span>↗</span><span>⊥</span><span>✕</span></div>
    <div class="tree">
      <div style="left:11px;top:53px"><b>▼</b><span style="width:10px">⋔</span>Bugbear</div>
      <div style="left:32px;top:74px"><b>▼</b><em></em>Pages</div>
      <div style="left:49px;top:94px"><b>▶</b><em style="height:8px"></em>Tracklog</div>
      <div style="left:49px;top:116px"><b>▶</b><em></em>AddBug</div>
      <div style="left:49px;top:138px"><b>▶</b><em></em>ViewBug</div>
      <div style="left:49px;top:161px"><b>▶</b><em></em>Types</div>
      <div style="left:32px;top:192px"><b>▶</b><em style="height:7px;width:11px"></em>Templates</div>
      <div style="left:49px;top:216px"><b>▶</b><span style="width:9px">⁄</span>Styles</div>
      <div style="left:49px;top:238px"><b>▶</b><span style="width:9px">⚙</span>Settings</div>
      <div style="left:32px;top:267px"><b>▶</b><em style="height:8px"></em>EmbeddedFiles</div>
      <div style="left:32px;top:294px"><b>▶</b><span style="width:9px">≡</span>Connectors</div>
    </div>
  </aside>

  <!-- working area -->
  <main class="abs canvas">
    <h2>VIEWBUG</h2>

    <div class="chip tail" style="left:61px;top:56px;width:92px"><svg class="tglyph" viewBox="0 0 13 12" fill="none" stroke="#fff" stroke-width="1.6"><path d="M1 2V1h11v1M6.5 1v10M4 11h5"/></svg>LABEL1</div>
    <div class="chip tail" style="left:163px;top:56px;width:137px"><svg class="tglyph" viewBox="0 0 13 12" fill="none" stroke="#fff" stroke-width="1.6"><path d="M1 2V1h11v1M6.5 1v10M4 11h5"/></svg>LAYOUTTABLE1</div>
    <div class="chip sel" style="left:312px;top:56px;width:137px"><svg class="tglyph" viewBox="0 0 13 12" fill="none" stroke="#fff" stroke-width="1.6"><path d="M1 2V1h11v1M6.5 1v10M4 11h5"/></svg>LAYOUTTABLE2</div>

    <div class="cell" style="left:54px;top:108px"><svg class="tglyph" viewBox="0 0 13 12" fill="none" stroke="#555" stroke-width="1.4"><path d="M1 2V1h11v1M6.5 1v10M4 11h5"/></svg>LayoutTable1</div>
    <div class="cell" style="left:190px;top:108px"><svg class="tglyph" viewBox="0 0 13 12" fill="none" stroke="#555" stroke-width="1.4"><path d="M1 2V1h11v1M6.5 1v10M4 11h5"/></svg>LayoutTable1</div>
    <div class="cell strong" style="left:328px;top:108px"><svg class="tglyph" viewBox="0 0 13 12" fill="none" stroke="#555" stroke-width="1.4"><path d="M1 2V1h11v1M6.5 1v10M4 11h5"/></svg>LAYOUTTABLE1</div>
    <div class="cell" style="left:54px;top:155px"><svg class="tglyph" viewBox="0 0 13 12" fill="none" stroke="#555" stroke-width="1.4"><path d="M1 2V1h11v1M6.5 1v10M4 11h5"/></svg>LayoutTable1</div>
    <div class="cell" style="left:190px;top:155px"><svg class="tglyph" viewBox="0 0 13 12" fill="none" stroke="#555" stroke-width="1.4"><path d="M1 2V1h11v1M6.5 1v10M4 11h5"/></svg>LayoutTable1</div>
    <div class="cell" style="left:328px;top:155px"><svg class="tglyph" viewBox="0 0 13 12" fill="none" stroke="#555" stroke-width="1.4"><path d="M1 2V1h11v1M6.5 1v10M4 11h5"/></svg>LayoutTable1</div>

    <div class="sep" style="top:222px"></div>
    <div class="chip tail" style="left:61px;top:244px;width:92px"><svg class="tglyph" viewBox="0 0 13 12" fill="none" stroke="#fff" stroke-width="1.6"><path d="M1 2V1h11v1M6.5 1v10M4 11h5"/></svg>LABEL1</div>
    <div class="chip sel" style="left:163px;top:244px;width:137px"><svg class="tglyph" viewBox="0 0 13 12" fill="none" stroke="#fff" stroke-width="1.6"><path d="M1 2V1h11v1M6.5 1v10M4 11h5"/></svg>LAYOUTTABLE1</div>
    <div class="cell" style="left:54px;top:299px"><svg class="tglyph" viewBox="0 0 13 12" fill="none" stroke="#555" stroke-width="1.4"><path d="M1 2V1h11v1M6.5 1v10M4 11h5"/></svg>LayoutTable1</div>
    <div class="cell" style="left:190px;top:299px"><svg class="tglyph" viewBox="0 0 13 12" fill="none" stroke="#555" stroke-width="1.4"><path d="M1 2V1h11v1M6.5 1v10M4 11h5"/></svg>LayoutTable1</div>
    <div class="cell" style="left:328px;top:299px"><svg class="tglyph" viewBox="0 0 13 12" fill="none" stroke="#555" stroke-width="1.4"><path d="M1 2V1h11v1M6.5 1v10M4 11h5"/></svg>LayoutTable1</div>

    <div class="sep" style="top:368px"></div>
    <div class="chip tail" style="left:61px;top:390px;width:92px"><svg class="tglyph" viewBox="0 0 13 12" fill="none" stroke="#fff" stroke-width="1.6"><path d="M1 2V1h11v1M6.5 1v10M4 11h5"/></svg>LABEL1</div>
    <div class="chip" style="left:163px;top:390px;width:137px"><svg class="tglyph" viewBox="0 0 13 12" fill="none" stroke="#fff" stroke-width="1.6"><path d="M1 2V1h11v1M6.5 1v10M4 11h5"/></svg>LAYOUTTABLE1</div>
    <div class="cell" style="left:54px;top:446px"><svg class="tglyph" viewBox="0 0 13 12" fill="none" stroke="#555" stroke-width="1.4"><path d="M1 2V1h11v1M6.5 1v10M4 11h5"/></svg>LayoutTable1</div>
    <div class="cell" style="left:190px;top:446px"><svg class="tglyph" viewBox="0 0 13 12" fill="none" stroke="#555" stroke-width="1.4"><path d="M1 2V1h11v1M6.5 1v10M4 11h5"/></svg>LayoutTable1</div>
    <div class="cell" style="left:328px;top:446px"><svg class="tglyph" viewBox="0 0 13 12" fill="none" stroke="#555" stroke-width="1.4"><path d="M1 2V1h11v1M6.5 1v10M4 11h5"/></svg>LayoutTable1</div>

    <div class="sep" style="top:510px"></div>
    <div class="chip tail" style="left:61px;top:532px;width:92px"><svg class="tglyph" viewBox="0 0 13 12" fill="none" stroke="#fff" stroke-width="1.6"><path d="M1 2V1h11v1M6.5 1v10M4 11h5"/></svg>LABEL1</div>
    <div class="chip sel" style="left:163px;top:532px;width:137px"><svg class="tglyph" viewBox="0 0 13 12" fill="none" stroke="#fff" stroke-width="1.6"><path d="M1 2V1h11v1M6.5 1v10M4 11h5"/></svg>LAYOUTTABLE1</div>
    <div class="cell" style="left:54px;top:588px"><svg class="tglyph" viewBox="0 0 13 12" fill="none" stroke="#555" stroke-width="1.4"><path d="M1 2V1h11v1M6.5 1v10M4 11h5"/></svg>LayoutTable1</div>
    <div class="cell" style="left:190px;top:588px"><svg class="tglyph" viewBox="0 0 13 12" fill="none" stroke="#555" stroke-width="1.4"><path d="M1 2V1h11v1M6.5 1v10M4 11h5"/></svg>LayoutTable1</div>
    <div class="cell" style="left:328px;top:588px"><svg class="tglyph" viewBox="0 0 13 12" fill="none" stroke="#555" stroke-width="1.4"><path d="M1 2V1h11v1M6.5 1v10M4 11h5"/></svg>LayoutTable1</div>
  </main>

  <!-- validations -->
  <section class="abs validations">
    <div class="val-head"><div class="tab">VALIDATIONS</div>
      <div class="pane-ctrls abs" style="left:453px;top:11px"><span>↗</span><span>⊥</span><span>✕</span></div></div>
    <div class="val-col-line"></div>
    <div class="val-label" style="left:15px;top:48px">DESCRIPTION</div>
    <div class="val-label" style="left:296px;top:48px">PATH</div>
    <div class="val-row" style="left:15px;top:80px"><span class="x">✕</span>No page has been linked</div>
    <div class="val-row" style="left:15px;top:127px"><span class="x">✕</span>No page has been linked</div>
    <div class="val-row" style="left:15px;top:174px"><span class="x">✕</span>No page has been linked</div>
    <div class="val-row" style="left:15px;top:221px"><span class="x">✕</span>No page has been linked</div>
    <div class="val-row" style="left:296px;top:72px">Pages &gt; StartPage &gt; Menu1 &gt; Menu Item 1&gt;<br>Destination Page</div>
    <div class="val-row" style="left:296px;top:119px">Pages &gt; StartPage &gt; Menu1 &gt; Menu Item 1&gt;<br>Destination Page</div>
    <div class="val-row" style="left:296px;top:166px">Pages &gt; StartPage &gt; Menu1 &gt; Menu Item 1&gt;<br>Destination Page</div>
    <div class="val-row" style="left:296px;top:213px">Pages &gt; StartPage &gt; Menu1 &gt; Menu Item 1&gt;<br>Destination Page</div>
  </section>

  <!-- toolbox and properties -->
  <aside class="abs toolbox">
    <div class="tab abs" style="left:0;top:0;width:130px">TOOLBOX</div>
    <div class="pane-ctrls abs" style="left:187px;top:9px"><span>↗</span><span>⊥</span><span>✕</span></div>
    <div class="viewbar" style="top:33px">VIEW</div>
    <div class="tools" style="top:49px">
      <div class="tool"><i style="border-radius:50%"></i>BUTTON</div>
      <div class="tool"><i style="border-top:0;border-right:0"></i>CHART</div>
      <div class="tool"><i></i>CHECK BOX</div>
      <div class="tool"><i></i>CHECK BOX</div>
      <div class="tool"><i style="border-width:3px 1.5px"></i>DATA GRID</div>
      <div class="tool"><i style="border-width:3px"></i>DATE PICKER</div>
      <div class="tool"><i style="border-width:2px 1.5px"></i>DROP DOWN</div>
      <div class="tool"><i></i>IMAGE</div>
      <div class="tool"><i style="border-radius:50% 50% 0 0"></i>LABEL</div>
      <div class="tool"><i style="border-radius:50%"></i>LINK</div>
      <div class="tool"><i style="border-top:0;border-right:0"></i>MENU</div>
      <div class="tool"><i style="transform:rotate(45deg);width:6px;height:6px"></i>PANEL</div>
      <div class="tool"><i style="transform:rotate(45deg);width:6px;height:6px"></i>RADIO BUTTON</div>
      <div class="tool"><i style="border-radius:3px"></i>REPEATER</div>
      <div class="tool"><i style="border-top-width:3px"></i>TEXT BOX</div>
      <div class="tool"><i style="border-radius:50% 50% 1px 1px"></i>UPLOAD FILE</div>
    </div>
    <div class="viewbar" style="top:220px">VIEW</div>
    <div class="tools" style="top:238px">
      <div class="tool"><i></i>CONTAINER</div>
      <div class="tool"><i style="background:#333"></i>FLEXBOX</div>
      <div class="tool"><i style="border-style:dotted;border-width:2px"></i>GRID</div>
      <div class="tool"><i></i>TABLE</div>
    </div>
    <div class="tab abs" style="left:0;top:280px;width:130px;height:32px">PROPERTIES</div>
    <div class="pane-ctrls abs" style="left:187px;top:290px"><span>↗</span><span>⊥</span><span>✕</span></div>
    <div class="props-label" style="left:19px;top:340px">Name</div>
    <div class="prop-input" style="left:77px;top:328px;width:161px">HistoryDataGrid</div>
    <div class="props-section" style="top:386px">DATA</div>
    <div class="props-label" style="left:19px;top:420px">Columns</div>
    <div class="prop-input" style="left:77px;top:408px;width:161px">(Collection)</div>
    <div class="props-section" style="top:466px">OPTIONAL</div>
    <div class="props-label" style="left:19px;top:500px;font-size:9px">Allow Export</div>
    <div class="prop-check" style="left:84px;top:495px"></div>
    <div class="props-label" style="left:118px;top:500px;font-size:9px">Display Search Bar</div>
    <div class="prop-check" style="left:213px;top:495px"></div>
    <div class="props-label" style="left:19px;top:533px;font-size:9px">Selectable Data</div>
    <div class="prop-check" style="left:95px;top:528px"></div>
    <div class="props-label" style="left:138px;top:533px;font-size:9px">Selectable Data</div>
    <div class="prop-check" style="left:213px;top:528px"></div>
    <div class="help-btn">PROPERTY HELP</div>
  </aside>
</section>

<!-- ================= Column editor ================= -->
<section class="board editor first">
  <div class="abs ed-bar">COLUMNS<div class="ctrls"><span>▢</span><span>✕</span></div></div>
  <div class="abs add-col">ADD COLUMN <svg width="9" height="6" viewBox="0 0 9 6" fill="none" stroke="#fff" stroke-width="1.5"><path d="M1 1l3.5 3.5L8 1"/></svg></div>
  <svg class="abs trash" viewBox="0 0 16 18" fill="none" stroke="#00b5d6" stroke-width="1.6"><path d="M1 3h14M6 3V1h4v2M3 3l1 14h8l1-14M6.5 6v8M9.5 6v8"/></svg>
  <div class="field" style="top:149px">First Name<svg viewBox="0 0 12 12"><circle cx="6" cy="3.5" r="3"/><path d="M0 12q0-5 6-5t6 5z"/></svg></div>
  <div class="field" style="top:200px">Last Name<svg viewBox="0 0 12 12"><circle cx="6" cy="3.5" r="3"/><path d="M0 12q0-5 6-5t6 5z"/></svg></div>
  <div class="field" style="top:251px">Age<svg viewBox="0 0 12 12"><path d="M1 0h7l3 3v9H1z"/></svg></div>
  <div class="field" style="top:302px">Height<svg viewBox="0 0 12 12"><path d="M8 1l3 3-7 7H1V8z"/></svg></div>

  <div class="group" style="top:85px">NAME</div>
  <div class="lbl" style="top:127px">COLUMN TYPE</div>
  <div class="input" style="top:116px">Data-Bound<svg class="chev" viewBox="0 0 8 5" fill="none" stroke="#666" stroke-width="1.2"><path d="M1 1l3 3 3-3"/></svg></div>
  <div class="lbl" style="top:175px">TEXT</div>
  <div class="input" style="top:164px">(Data-Bound)<svg class="chev" viewBox="0 0 8 5" fill="none" stroke="#666" stroke-width="1.2"><path d="M1 1l3 3 3-3"/></svg></div>
  <div class="group" style="top:232px">EVENTS</div>
  <div class="lbl" style="top:274px">CLICK</div>
  <div class="action" style="top:263px">CREATEEVENTHANDLER</div>
  <div class="group" style="top:327px">NAME</div>
  <div class="lbl" style="top:369px">HEADER TEXT</div>
  <div class="input" style="top:358px">First Name<svg class="chev" viewBox="0 0 8 5" fill="none" stroke="#666" stroke-width="1.2"><path d="M1 1l3 3 3-3"/></svg></div>
  <div class="lbl" style="top:417px">ALIGNMENT</div>
  <div class="input" style="top:406px">Left<svg class="chev" viewBox="0 0 8 5" fill="none" stroke="#666" stroke-width="1.2"><path d="M1 1l3 3 3-3"/></svg></div>
  <div class="lbl" style="top:465px">CELL DISPLAY</div>
  <div class="input" style="top:454px">Default<svg class="chev" viewBox="0 0 8 5" fill="none" stroke="#666" stroke-width="1.2"><path d="M1 1l3 3 3-3"/></svg></div>
  <div class="lbl" style="top:513px">ALIGNMENT</div>
  <div class="checkbox" style="top:502px"><svg width="11" height="9" viewBox="0 0 11 9" fill="none" stroke="#555" stroke-width="2"><path d="M1 4.5l3 3L10 1"/></svg></div>

  <div class="footer">
    <h3>COLUMN TYPE</h3>
    <p>CHOOSE WHETHER THE CELL DISPLAYS A VALUE FROM A CONNECTOR OR THE SPECIFIED TEXT</p>
    <div class="btn save">SAVE</div>
    <div class="btn cancel">CANCEL</div>
  </div>
</section>

<!-- ================= Column editor with expression picker ================= -->
<section class="board editor second">
  <div class="abs ed-bar">COLUMNS<div class="ctrls"><span>▢</span><span>✕</span></div></div>
  <div class="abs add-col">ADD COLUMN <svg width="9" height="6" viewBox="0 0 9 6" fill="none" stroke="#fff" stroke-width="1.5"><path d="M1 1l3.5 3.5L8 1"/></svg></div>
  <svg class="abs trash" viewBox="0 0 16 18" fill="none" stroke="#00b5d6" stroke-width="1.6"><path d="M1 3h14M6 3V1h4v2M3 3l1 14h8l1-14M6.5 6v8M9.5 6v8"/></svg>
  <div class="field" style="top:149px">First Name<svg viewBox="0 0 12 12"><circle cx="6" cy="3.5" r="3"/><path d="M0 12q0-5 6-5t6 5z"/></svg></div>
  <div class="field" style="top:200px">Last Name<svg viewBox="0 0 12 12"><circle cx="6" cy="3.5" r="3"/><path d="M0 12q0-5 6-5t6 5z"/></svg></div>
  <div class="field" style="top:251px">Age<svg viewBox="0 0 12 12"><path d="M1 0h7l3 3v9H1z"/></svg></div>
  <div class="field" style="top:302px">Height<svg viewBox="0 0 12 12"><path d="M8 1l3 3-7 7H1V8z"/></svg></div>

  <div class="group" style="top:85px">NAME</div>
  <div class="lbl" style="top:127px">COLUMN TYPE</div>
  <div class="input" style="top:116px">Data-Bound<svg class="chev" viewBox="0 0 8 5" fill="none" stroke="#666" stroke-width="1.2"><path d="M1 1l3 3 3-3"/></svg></div>
  <div class="lbl" style="top:175px">TEXT</div>
  <div class="input" style="top:164px">(Data-Bound)<svg class="chev" viewBox="0 0 8 5" fill="none" stroke="#666" stroke-width="1.2"><path d="M1 1l3 3 3-3"/></svg></div>
  <div class="group" style="top:232px">EVENTS</div>
  <div class="lbl" style="top:274px">CLICK</div>
  <div class="action" style="top:263px">CREATEEVENTHANDLER</div>
  <div class="group" style="top:327px">NAME</div>
  <div class="lbl" style="top:369px">HEADER TEXT</div>
  <div class="input" style="top:358px;width:245px">First Name<span style="margin-left:auto;font-size:11px;font-weight:700;color:#444">X<sup style="font-size:6px">²</sup></span></div>
  <div class="expr-toggle" style="top:358px"><svg width="10" height="6" viewBox="0 0 10 6" fill="none" stroke="#fff" stroke-width="1.6"><path d="M1 5l4-4 4 4"/></svg></div>
  <div class="lbl" style="top:417px">ALIGNMENT</div>
  <div class="lbl" style="top:465px">CELL DISPLAY</div>
  <div class="lbl" style="top:513px">ALIGNMENT</div>

  <div class="expr">
    <h4>X<sup>²</sup> EXPRESSION</h4>
    <div class="node" style="left:18px;top:47px"><span class="caret"></span>Session</div>
    <div class="node active" style="left:38px;top:72px"><span class="caret blue"></span>LoggedInUser</div>
    <div class="node" style="left:59px;top:96px"><span class="dot"></span>ID</div>
    <div class="node" style="left:59px;top:120px"><span class="dot"></span>Name</div>
    <div class="node" style="left:59px;top:143px"><span class="dot"></span>Email</div>
    <div class="node" style="left:59px;top:167px"><span class="dot"></span>Roles</div>
  </div>

  <div class="footer">
    <h3>COLUMN TYPE</h3>
    <p>CHOOSE WHETHER THE CELL DISPLAYS A VALUE FROM A CONNECTOR OR THE SPECIFIED TEXT</p>
    <div class="btn save">SAVE</div>
    <div class="btn cancel">CANCEL</div>
  </div>
</section>

</body>
</html>
```